Marrowfield Benefit Advisors Business Card Design

I already placed order for cards through sketch hive.

Double sided- back Navy with White logo and raised silver "swoosh"

```html
<!DOCTYPE html>
<html lang="en">
<head>
<meta charset="utf-8">
<title>Marrowfield Benefit Advisors – Business Card</title>
<link rel="stylesheet" href="https://fonts.googleapis.com/css2?family=Montserrat:wght@400;500;700&display=swap">
<style>
  :root {
    --page-bg: #e9e4dc;
    --card-bg: #e6dccd;
    --card-edge: #f4efe7;
    --navy: #1d2b45;
    --ink: #1f2230;
    --bar-grey-top: #948e86;
    --bar-grey-bottom: #4f4a45;
  }
  html, body {
    margin: 0;
    padding: 0;
    width: 1200px;
    height: 1047px;
    overflow: hidden;
    background: var(--page-bg);
    font-family: "Montserrat", sans-serif;
  }
  .card {
    position: absolute;
    left: 100px;
    top: 251px;
    width: 1000px;
    height: 546px;
    border-radius: 28px;
    background: var(--card-bg);
    box-shadow: inset 0 0 0 2px var(--card-edge), 0 12px 40px rgba(60, 50, 40, 0.15);
    color: var(--ink);
  }
  .accent-bar-left {
    position: absolute;
    left: 0;
    top: 125px;
    width: 41px;
    height: 296px;
    background: var(--navy);
  }
  .accent-bar-right {
    position: absolute;
    left: 968px;
    top: 130px;
    width: 32px;
    height: 291px;
    background: linear-gradient(180deg, var(--bar-grey-top), var(--bar-grey-bottom));
  }
  .brand {
    position: absolute;
    left: 74px;
    top: 248px;
    display: flex;
    align-items: center;
    gap: 14px;
  }
  .brand-mark {
    width: 26px;
    height: 26px;
    background: var(--navy);
  }
  .brand-name {
    font-weight: 700;
    font-size: 22px;
    color: var(--navy);
    letter-spacing: 0.5px;
    white-space: nowrap;
  }
  .divider {
    position: absolute;
    left: 520px;
    top: 125px;
    width: 2px;
    height: 296px;
    background: var(--navy);
  }
  .details {
    position: absolute;
    left: 556px;
    top: 118px;
  }
  .person-name {
    margin: 0;
    font-weight: 700;
    font-size: 43px;
    letter-spacing: 1px;
    color: var(--navy);
    line-height: 1.15;
  }
  .person-title {
    margin: 2px 0 0;
    font-weight: 500;
    font-size: 25px;
    line-height: 1.3;
  }
  .address {
    margin: 20px 0 0;
    font-weight: 500;
    font-size: 25px;
    line-height: 1.5;
    font-style: normal;
  }
  .contact-list {
    list-style: none;
    margin: 12px 0 0;
    padding: 0;
  }
  .contact-list li {
    display: flex;
    align-items: center;
    gap: 12px;
    font-weight: 500;
    font-size: 25px;
    line-height: 38px;
  }
  .contact-icon {
    width: 20px;
    height: 20px;
    flex: none;
  }
</style>
</head>
<body>
  <div class="card">
    <div class="accent-bar-left"></div>

    <div class="brand">
      <span class="brand-mark"></span>
      <span class="brand-name">Marrowfield Benefit Advisors</span>
    </div>

    <div class="divider"></div>

    <div class="details">
      <h1 class="person-name">MARTIN KELLER</h1>
      <p class="person-title">Managing Director</p>
      <address class="address">Your address, City<br>State, Zip 1234</address>
      <ul class="contact-list">
        <li>
          <svg class="contact-icon" viewBox="0 0 20 20" aria-hidden="true">
            <path fill="#1f2230" d="M2 7c0-2 3-4 8-4s8 2 8 4v2h-4V7.5c-1-.6-2.4-.9-4-.9s-3 .3-4 .9V9H2z"/>
            <path fill="#1f2230" d="M6 9.5l1.5-2h5l1.5 2 2 2V17H4v-5.5z"/>
            <circle cx="10" cy="13" r="2" fill="#e6dccd"/>
          </svg>
          123 456 789
        </li>
        <li>
          <svg class="contact-icon" viewBox="0 0 20 20" aria-hidden="true">
            <rect x="2" y="5" width="16" height="11" rx="1" fill="#1f2230"/>
            <path d="M2.5 5.5 10 11l7.5-5.5" fill="none" stroke="#e6dccd" stroke-width="1.4"/>
          </svg>
          info@youremail.com
        </li>
        <li>
          <svg class="contact-icon" viewBox="0 0 20 20" aria-hidden="true">
            <circle cx="10" cy="10" r="8" fill="#1f2230"/>
            <path d="M6 6.5c1.5 0 2 1 3 1.5s.5 2-1 2.5-1 2.5-2 3M12 4.5c0 1.5 1 2 2 2.5s1.5 2.5 0 3.5-1 3-2 4" fill="none" stroke="#e6dccd" stroke-width="1.3"/>
          </svg>
          www.yourwebsite.com
        </li>
      </ul>
    </div>

    <div class="accent-bar-right"></div>
  </div>
</body>
</html>
```